Flyer Design Project

Just needing a sleek, modern brochure design for my Paint Contracting business. It's a one sided leaflet (99mm X 210mm)

Brennick Finish Coatings
"Over 25 years experience"
"We set the standard for quality and service"

Call for a free estimate:
Dorian Vellacott 0438195026
Dorianvellacott0@mailbox-example.com
http://brennickfinishcoatings.sitenest-example.com.au/

All Painting services offered:
Interior, exterior, pressure washing, staing, roof restoration, residential, commercial and body corporate

Target Market(s)

Home owners

Industry/Entity Type

Business

```html
<!DOCTYPE html>
<html lang="en">
<head>
<meta charset="utf-8">
<title>Brennick Finish Coatings – Leaflet</title>
<link rel="stylesheet" href="https://fonts.googleapis.com/css2?family=Anton&family=Marcellus&family=Arimo&family=Cousine&family=Tinos&display=swap">
<style>
  :root {
    --page: #ffffff;
    --paper: #f8f6f3;
    --crimson: #d8345e;
    --crimson-deep: #c42a52;
    --teal: #3cc0b3;
    --ink: #151515;
    --body: #2a2a2a;
    --url-wash: #d9f1ee;
    --photo-top: #e9e4dc;
    --photo-mid: #7fcfc4;
    --photo-low: #e45384;
    --photo-floor: #d9d6d2;
  }
  * { box-sizing: border-box; margin: 0; padding: 0; }
  html, body { width: 1200px; height: 1000px; overflow: hidden; background: var(--page); }
  .canvas { position: relative; width: 1200px; height: 1000px; }

  .leaflet {
    position: absolute; left: 390px; top: 54px;
    width: 420px; height: 892px;
    background: var(--paper);
    overflow: hidden;
  }

  .hero-photo {
    position: absolute; left: 0; top: 0; width: 420px; height: 360px;
    background:
      radial-gradient(ellipse 45% 40% at 30% 45%, var(--photo-mid) 0%, transparent 70%),
      radial-gradient(ellipse 40% 40% at 78% 50%, var(--photo-low) 0%, transparent 70%),
      linear-gradient(180deg, var(--photo-top) 0%, #d7cfc4 40%, var(--photo-floor) 100%);
  }

  .brand-band { position: absolute; left: 0; top: 338px; width: 420px; height: 160px; }
  .brand-band svg { position: absolute; inset: 0; }
  .brand-name {
    position: absolute; left: 0; right: 0; top: 30px;
    text-align: center; color: #fff;
    font-family: "Marcellus", serif; font-weight: 400;
  }
  .brand-name .line-1 { display: block; font-size: 50px; letter-spacing: 1px; line-height: 1; }
  .brand-name .line-2 { display: block; font-size: 30px; line-height: 1.25; margin-top: 4px; }

  .content { position: absolute; left: 30px; right: 20px; top: 520px; }
  .headline {
    font-family: "Anton", sans-serif; font-weight: 400;
    text-transform: uppercase; line-height: 1.1;
  }
  .experience { color: var(--crimson); font-size: 27px; }
  .standard { color: var(--ink); font-size: 25px; margin-top: 16px; }
  .estimate { color: var(--crimson); font-size: 26px; margin-top: 16px; }
  .contact { margin-top: 10px; font-family: "Arimo", sans-serif; font-size: 14.5px; color: var(--ink); line-height: 1.3; }
  .contact .web {
    display: inline-block; margin-left: -6px; padding: 1px 6px;
    font-family: "Cousine", monospace; font-size: 11.6px;
    background: var(--url-wash);
  }
  .services-title { color: var(--teal); font-size: 21px; margin-top: 14px; line-height: 1.05; }
  .services-list {
    margin-top: 6px; font-family: "Tinos", serif; font-size: 15px;
    color: var(--body); line-height: 1.2; max-width: 300px;
  }
</style>
</head>
<body>
<div class="canvas">
  <article class="leaflet">
    <div class="hero-photo" role="img" aria-label="Photograph of several paint tins in teal, pink and blue on a workbench"></div>

    <header class="brand-band">
      <svg width="420" height="160" viewBox="0 0 420 160" aria-hidden="true">
        <path d="M0 14 Q40 4 90 12 T200 8 T320 14 T420 6 V146 Q360 152 300 142 T180 150 T60 142 T0 150 Z" fill="var(--crimson)"/>
        <path d="M0 138 Q80 150 160 140 T320 146 T420 136 V150 Q330 160 240 150 T80 156 T0 150 Z" fill="var(--crimson-deep)" opacity="0.6"/>
      </svg>
      <h1 class="brand-name">
        <span class="line-1">BRENNICK</span>
        <span class="line-2">Finish Coatings</span>
      </h1>
    </header>

    <section class="content">
      <p class="headline experience">Over 25 years experience</p>
      <p class="headline standard">We set the standard<br>for quality and service</p>
      <p class="headline estimate">Call for a free estimate:</p>
      <address class="contact" style="font-style:normal">
        Dorian Vellacott 0438195026<br>
        Dorianvellacott0@mailbox-example.com<br>
        <span class="web">http://brennickfinishcoatings.sitenest-example.com.au/</span>
      </address>
      <p class="headline services-title">All painting<br>services offered:</p>
      <p class="services-list">Interior, exterior, pressure washing, staining, roof restoration, residential, commercial and body corporate</p>
    </section>
  </article>
</div>
</body>
</html>
```